Business Card & Stationary
Powder Coating Company
Project: Business Card & Stationary
Business Card & Stationary - Miscellaneous
Creative Brief
Professional
Rutger Vandelow
Owner / Operator
4715 Ave K 1/2
nullemail@brindlecoatfinish.com
www.brindlecoatfinish.com
Should list our services, which include Powder Coating, Ceramic Coating and Abrasive Blasting

```html
<!DOCTYPE html>
<html lang="en">
<head>
<meta charset="utf-8">
<title>Brindlecoat Finish – Business Card</title>
<link rel="stylesheet" href="https://fonts.googleapis.com/css2?family=Open+Sans:wght@400;600;700;800&display=swap">
<style>
  :root {
    --page-bg: #e9e6e2;
    --card-white: #ffffff;
    --brand-red: #c8141a;
    --brand-red-dark: #8e0b10;
    --swoosh-black: #141414;
    --ink: #3a3a3a;
    --rule: #b9b9b9;
  }
  * { box-sizing: border-box; margin: 0; padding: 0; }
  html, body {
    width: 1200px; height: 780px; overflow: hidden;
    background: var(--page-bg);
    font-family: "Open Sans", Arial, sans-serif;
  }
  .card {
    position: absolute; left: 100px; top: 104px;
    width: 1000px; height: 572px;
    background: var(--card-white);
    border-radius: 34px;
    overflow: hidden;
    box-shadow: 0 14px 36px rgba(0,0,0,.22);
  }
  .card__header-art { position: absolute; inset: 0; width: 100%; height: 100%; }
  .card__person {
    position: absolute; right: 44px; top: 34px;
    text-align: right; color: #fff;
  }
  .card__name { font-size: 32px; font-weight: 700; letter-spacing: .2px; }
  .card__role { font-size: 21px; font-weight: 400; margin-top: 4px; }
  .card__brand {
    position: absolute; left: 70px; top: 360px;
    display: flex; align-items: center; gap: 16px;
  }
  .card__brand-dot {
    width: 26px; height: 26px; border-radius: 50%;
    background: var(--brand-red);
  }
  .card__brand-name {
    font-size: 46px; font-weight: 800; color: var(--brand-red);
    letter-spacing: -.5px;
  }
  .card__contact {
    position: absolute; left: 598px; top: 308px;
    padding-left: 24px;
    border-left: 2px solid var(--rule);
    color: var(--ink); font-size: 21px; line-height: 1;
  }
  .contact__row { display: flex; align-items: center; gap: 12px; height: 38px; }
  .contact__row--address { margin-bottom: 8px; }
  .contact__icon { width: 20px; height: 20px; flex: none; }
</style>
</head>
<body>
  <article class="card">
    <svg class="card__header-art" viewBox="0 0 1000 572" preserveAspectRatio="none" aria-hidden="true">
      <defs>
        <linearGradient id="headerRed" x1="0" y1="0" x2="0" y2="1">
          <stop offset="0" stop-color="#e01b22"/>
          <stop offset="1" stop-color="#9c0c11"/>
        </linearGradient>
      </defs>
      <path d="M0 0 H1000 V168 C760 160 420 190 0 226 Z" fill="url(#headerRed)"/>
      <path d="M0 226 C420 190 760 160 1000 168 C760 172 430 212 0 262 Z" fill="var(--swoosh-black)"/>
    </svg>

    <div class="card__person">
      <div class="card__name">Rutger Vandelow</div>
      <div class="card__role">Owner / Operator</div>
    </div>

    <div class="card__brand">
      <span class="card__brand-dot"></span>
      <span class="card__brand-name">Brindlecoat Finish</span>
    </div>

    <div class="card__contact">
      <div class="contact__row contact__row--address">4715 Ave K 1/2</div>
      <div class="contact__row">
        <svg class="contact__icon" viewBox="0 0 20 20" aria-hidden="true">
          <path d="M5 2 L8 2 L9 6 L7 7.5 C8 10 10 12 12.5 13 L14 11 L18 12 L18 15 C18 16.5 16.5 18 15 18 C8 18 2 12 2 5 C2 3.5 3.5 2 5 2 Z" fill="var(--brand-red)"/>
        </svg>
        (409) 555-0147
      </div>
      <div class="contact__row">
        <svg class="contact__icon" viewBox="0 0 20 20" aria-hidden="true">
          <rect x="5" y="2" width="10" height="6" fill="var(--brand-red)"/>
          <rect x="2" y="8" width="16" height="7" rx="1.5" fill="var(--brand-red)"/>
          <rect x="5" y="13" width="10" height="5" fill="var(--brand-red)"/>
        </svg>
        (409) 555-0193
      </div>
      <div class="contact__row">
        <svg class="contact__icon" viewBox="0 0 20 20" aria-hidden="true">
          <circle cx="10" cy="10" r="8" fill="none" stroke="var(--brand-red)" stroke-width="2"/>
          <ellipse cx="10" cy="10" rx="3.5" ry="8" fill="none" stroke="var(--brand-red)" stroke-width="1.5"/>
          <line x1="2" y1="10" x2="18" y2="10" stroke="var(--brand-red)" stroke-width="1.5"/>
        </svg>
        brindlecoatfinish.com
      </div>
    </div>
  </article>
</body>
</html>
```